BrimTaps.com

Hey guys!

We are looking for an innovative 1 page web design for our PPC network website - http://quillpixelgrab.example/4k2n8dwq7z
We are a PPC social media start up, which works with many social media publishers worldwide.
The design must be clean, flat, trendy, we would like to keep our 1 page design structure, but add your own personal touch-up.

We would like you to make it look like a Million $ company.

Good luck!

Target Market(s)

Big Internet Advertising Companies

Number of Pages Required

1 page

```html
<!DOCTYPE html>
<html lang="en">
<head>
<meta charset="utf-8">
<title>Social Media Enterprise</title>
<link rel="stylesheet" href="https://fonts.googleapis.com/css2?family=Arimo:ital,wght@0,400;0,700;1,400;1,700&family=Open+Sans:wght@400;600;700&family=Yanone+Kaffeesatz:wght@600&display=swap">
<style>
:root{
  --brand-blue:#2f20f5;
  --bar-dark:#1a1a1a;
  --section-dark:#222222;
  --panel-green:#a0fb80;
  --panel-green-edge:#6fcf55;
  --tile-grey:#6b6b6b;
  --card-lilac:#d6d2f8;
  --avatar:#9b8ff0;
  --ink:#111111;
  --ink-navy:#1d1a7a;
  --white:#ffffff;
  --chip:#7d7d86;
}
*{box-sizing:border-box;margin:0;padding:0}
html,body{width:1200px;height:1000px;overflow:hidden;background:var(--white)}
body{position:relative;font-family:"Arimo",Arial,sans-serif;color:var(--ink)}
.abs{position:absolute}

/* header */
.hero{left:271px;top:0;width:657px;height:292px;background:var(--brand-blue)}
.logo-text{left:40px;top:25px;font-size:16px;color:var(--white)}
.site-title{left:157px;top:28px;font-size:28px;color:var(--white);font-weight:400}
.globe{left:66px;top:50px;width:234px;height:208px;border-radius:50%;
  background:radial-gradient(circle at 45% 40%,#7fe0f0 0%,#2aa6d6 45%,#1b5fa8 100%)}
.hero-copy{left:350px;top:115px;width:266px;font-size:7.6px;line-height:1.3;color:var(--white)}
.main-nav{left:357px;top:262px;display:flex;gap:0;font-family:"Yanone Kaffeesatz","Oswald",sans-serif;font-weight:600;font-size:15px;color:var(--white)}
.main-nav span{position:absolute;white-space:nowrap}

/* share bar */
.share-bar{left:271px;top:292px;width:657px;height:36px;background:var(--bar-dark)}
.share-list{left:102px;top:4px;display:flex;gap:1px}
.share-chip{width:28px;height:28px;border-radius:4px;background:var(--chip);border:1px solid #a5a5ad}

/* features */
.feature{width:152px}
.feature-thumb{width:123px;height:68px;border-radius:4px;border:5px solid #3a3a3a;background:linear-gradient(135deg,#0a0a0a,#1e3b55 55%,#0a0a0a)}
.feature-title{margin-top:10px;font-weight:700;font-style:italic;font-size:11px}
.feature-copy{margin-top:4px;font-size:6.6px;line-height:1.35;text-align:justify}

/* info section */
.info{left:267px;top:583px;width:666px;height:345px;background:var(--section-dark)}
.tagline{left:4px;top:4px;width:658px;height:35px;background:var(--bar-dark);color:var(--white);
  font-style:italic;font-size:11px;text-align:center;line-height:35px}
.col-heading{top:69px;font-family:"Open Sans",sans-serif;font-weight:600;font-size:13px;color:var(--white)}
.panel{top:92px;width:176px;height:217px;background:var(--panel-green);border-left:4px solid var(--panel-green-edge)}
.read-tile{left:11px;width:146px;height:34px;background:var(--tile-grey);border:1px solid #8a8a8a;
  font-size:5.6px;font-style:italic;color:var(--ink-navy);padding:13px 6px 0}
.comment-card{left:4px;width:155px;height:55px;background:var(--card-lilac);border:2px solid var(--white);border-radius:7px}
.avatar{left:6px;top:4px;width:20px;height:20px}
.comment-text{left:30px;top:3px;width:121px;font-size:5px;line-height:1.25;text-align:justify;color:#222}
.comment-meta{left:30px;top:43px;width:121px;font-size:5px;font-style:italic;color:#333;display:flex;justify-content:space-between}
.comment-meta u{color:var(--ink-navy)}
.scrollbar{left:162px;top:14px;width:4px;height:196px;background:#333;border-radius:2px}
.event{left:13px;width:152px}
.event-title{font-family:"Open Sans",sans-serif;font-weight:700;font-size:8px}
.event-place{font-family:"Open Sans",sans-serif;font-weight:700;font-size:6.4px;margin-top:2px}
.event-copy{font-size:5px;line-height:1.3;color:#224;margin-top:3px}
.event-date{font-size:5px;color:#224;margin-top:6px}
</style>
</head>
<body>

<header class="abs hero">
  <div class="abs logo-text">Logo</div>
  <div class="abs globe" role="img" aria-label="Illustrated globe with orbit ring and hand cursor"></div>
  <h1 class="abs site-title">Social Media Enterprise</h1>
  <p class="abs hero-copy">Lorem ipsum dolor sit amet, consectetur adipisicing elit, sed do eiusmod tempor incididunt ut labore et dolore magna aliqua. Ut enim ad minim veniam, quis nostrud exercitation ullamco laboris nisi ut aliquip ex ea commodo consequat. Duis aute irure dolor in reprehenderit in voluptate velit esse cillum dolore eu fugiat nulla pariatur. Excepteur sint occaecat cupidatat non proident, sunt in culpa qui officia deserunt mollit anim id est laborum.</p>
  <nav class="abs main-nav">
    <span style="left:0">Home</span>
    <span style="left:48px">Services</span>
    <span style="left:112px">Process</span>
    <span style="left:173px">Help</span>
    <span style="left:219px">About US</span>
  </nav>
</header>

<div class="abs share-bar">
  <div class="abs share-list">
    <i class="share-chip"></i><i class="share-chip"></i><i class="share-chip"></i><i class="share-chip"></i><i class="share-chip"></i>
    <i class="share-chip"></i><i class="share-chip"></i><i class="share-chip"></i><i class="share-chip"></i><i class="share-chip"></i>
    <i class="share-chip"></i><i class="share-chip"></i><i class="share-chip"></i><i class="share-chip"></i><i class="share-chip"></i>
  </div>
</div>

<section class="abs feature" style="left:346px;top:352px">
  <div class="feature-thumb" role="img" aria-label="Glowing blue keyboard photo"></div>
  <h2 class="feature-title">Marketing</h2>
  <p class="feature-copy">Lorem ipsum dolor sit amet, consectetur adipisicing elit, sed do eiusmod tempor incididunt ut labore et dolore magna aliqua. Ut enim ad minim veniam, quis nostrud exercitation ullamco laboris nisi ut aliquip ex ea commodo consequat.</p>
</section>
<section class="abs feature" style="left:539px;top:352px">
  <div class="feature-thumb" role="img" aria-label="Data analytics light display photo" style="background:linear-gradient(180deg,#1a1040,#a0402a 55%,#10121a)"></div>
  <h2 class="feature-title">Analytics</h2>
  <p class="feature-copy">Lorem ipsum dolor sit amet, consectetur adipisicing elit, sed do eiusmod tempor incididunt ut labore et dolore magna aliqua. Ut enim ad minim veniam, quis nostrud exercitation ullamco laboris nisi ut aliquip ex ea commodo consequat.</p>
</section>
<section class="abs feature" style="left:733px;top:352px">
  <div class="feature-thumb" role="img" aria-label="Wall of media screens photo" style="background:linear-gradient(135deg,#3a2a20,#7a5a40 50%,#1a1a2a)"></div>
  <h2 class="feature-title">Media</h2>
  <p class="feature-copy">Lorem ipsum dolor sit amet, consectetur adipisicing elit, sed do eiusmod tempor incididunt ut labore et dolore magna aliqua. Ut enim ad minim veniam, quis nostrud exercitation ullamco laboris nisi ut aliquip ex ea commodo consequat.</p>
</section>

<section class="abs info">
  <p class="abs tagline">We are a PPC social media start up, which works with many social media publishers worldwide.</p>

  <h3 class="abs col-heading" style="left:33px">Most read</h3>
  <h3 class="abs col-heading" style="left:260px">Comments</h3>
  <h3 class="abs col-heading" style="left:474px">Upcomming Events</h3>

  <div class="abs panel" style="left:33px">
    <div class="abs read-tile" style="top:22px">PPC Market Evolution</div>
    <div class="abs read-tile" style="top:72px">500 Fortune most sucess enterprise</div>
    <div class="abs read-tile" style="top:122px">International online trading</div>
    <div class="abs read-tile" style="top:172px">SEO - New features</div>
  </div>

  <div class="abs panel" style="left:260px">
    <article class="abs comment-card" style="top:12px">
      <svg class="abs avatar" viewBox="0 0 20 20"><circle cx="10" cy="6" r="5" fill="var(--avatar)"/><rect x="1" y="12" width="18" height="8" rx="4" fill="var(--avatar)"/></svg>
      <p class="abs comment-text">Lorem ipsum dolor sit amet, consectetur adipisicing elit, sed do eiusmod tempor incididunt ut labore et dolore magna aliqua. Ut enim ad minim veniam, quis nostrud exercitation ullamco laboris nisi ut aliquip ex ea commodo consequat.</p>
      <p class="abs comment-meta"><span>Posted by: Jon L.&nbsp;&nbsp; 10 hours ago</span><span><u>Reply</u> <u>Like</u></span></p>
    </article>
    <article class="abs comment-card" style="top:84px">
      <svg class="abs avatar" viewBox="0 0 20 20"><circle cx="10" cy="6" r="5" fill="var(--avatar)"/><rect x="1" y="12" width="18" height="8" rx="4" fill="var(--avatar)"/></svg>
      <p class="abs comment-text">Lorem ipsum dolor sit amet, consectetur adipisicing elit, sed do eiusmod tempor incididunt ut labore et dolore magna aliqua. Ut enim ad minim veniam, quis nostrud exercitation ullamco laboris nisi ut aliquip ex ea commodo consequat.</p>
      <p class="abs comment-meta"><span>Posted by: Jean&nbsp;&nbsp; 3 hours ago</span><span><u>Reply</u> <u>Like</u></span></p>
    </article>
    <article class="abs comment-card" style="top:154px">
      <svg class="abs avatar" viewBox="0 0 20 20"><circle cx="10" cy="6" r="5" fill="var(--avatar)"/><rect x="1" y="12" width="18" height="8" rx="4" fill="var(--avatar)"/></svg>
      <p class="abs comment-text">Lorem ipsum dolor sit amet, consectetur adipisicing elit, sed do eiusmod tempor incididunt ut labore et dolore magna aliqua. Ut enim ad minim veniam, quis nostrud exercitation ullamco laboris nisi ut aliquip ex ea commodo consequat.</p>
      <p class="abs comment-meta"><span>Posted by: Anne.&nbsp;&nbsp; 10 hours ago</span><span><u>Reply</u> <u>Like</u></span></p>
    </article>
    <div class="abs scrollbar"></div>
  </div>

  <div class="abs panel" style="left:474px">
    <div class="abs event" style="top:13px">
      <p class="event-title">SAT - Conference</p>
      <p class="event-place">Toronto - Canada</p>
      <p class="event-copy">Lorem ipsum dolor sit amet, consectetur adipisicing elit, sed do eiusmod tempor incididunt ut labore et dolore magna.</p>
      <p class="event-date">September 15th, 2015</p>
    </div>
    <div class="abs event" style="top:85px">
      <p class="event-title">Internet Webinar</p>
      <p class="event-place">Nimbus Hub</p>
      <p class="event-copy">Lorem ipsum dolor sit amet, consectetur adipisicing elit, sed do eiusmod tempor incididunt ut labore et dolore magna.</p>
      <p class="event-date">October 8th, 2015</p>
    </div>
    <div class="abs event" style="top:156px">
      <p class="event-title">World Expo - IP</p>
      <p class="event-place">London - Great Britain</p>
      <p class="event-copy">Lorem ipsum dolor sit amet, consectetur adipisicing elit, sed do eiusmod tempor incididunt ut labore et dolore magna.</p>
      <p class="event-date">December 4th, 2015</p>
    </div>
  </div>
</section>

</body>
</html>
```